Restaurant service company needs a website!

I am looking for a skilled web designer/developer to create a professional, responsive, and easy-to-navigate website for my company, which specializes in servicing restaurant cooking equipment. The site should communicate trust, reliability, and technical expertise to our target audience, restaurant owners, managers, and commercial kitchen operators. I have included the company logos, if any other format for them is needed please let me know.

Target Market(s)

restaurant owners, managers, and commercial kitchen operators

Industry/Entity Type

Commercial Kitchen Equipment Service

Coding

Coded - Design and coding required

Number of Pages Required

1 page

Font styles to use
Serif
Sans Serif

Requirements
Must have
• Contact and service request forms, Click-to-call functionality for mobile, Clean, modern layout with strong visuals, Easy navigation, mobile-friendly
Nice to have
• Testimonials or Reviews, If possible a click-to-text functionality for mobile.
Should not have
• Any mention of Refrigeration or HVAC, "Free Quotes"

```html
<!DOCTYPE html>
<html lang="en">
<head>
<meta charset="utf-8">
<title>Hearthline Website – UX / UI Design &amp; Frontend Developing</title>
<link rel="stylesheet" href="https://fonts.googleapis.com/css2?family=Barlow:ital,wght@0,400;0,500;0,600;0,700;0,800;1,300&family=Inter:wght@400;500;600;700&display=swap">
<style>
:root{
  --board:#2b7a8c;
  --teal:#0e6478;
  --teal-deep:#0a5567;
  --teal-soft:#1d7b90;
  --ink:#14212b;
  --muted:#6f7d86;
  --sky:#eaf4fa;
  --sky-2:#dcecf5;
  --white:#ffffff;
  --line:#d6e4ec;
  --head:'Barlow',sans-serif;
  --body:'Inter',sans-serif;
}
*{box-sizing:border-box;margin:0;padding:0}
html,body{width:1200px;height:4229px;overflow:hidden}
body{background:var(--board);font-family:var(--body);color:var(--ink);position:relative}

/* board header */
.board-title{position:absolute;top:58px;left:0;width:1200px;text-align:center;color:var(--white)}
.board-title h1{font-family:var(--head);font-weight:800;font-size:40px;letter-spacing:.5px}
.board-title p{font-family:var(--head);font-style:italic;font-weight:300;font-size:38px;margin-top:4px}
.tools{position:absolute;top:180px;left:460px;display:flex;gap:11px}
.tools span{width:36px;height:36px;border-radius:7px;background:var(--white)}

/* ===== desktop frame ===== */
.desk{position:absolute;left:71px;top:271px;width:804px;height:3720px;background:var(--white);overflow:hidden}
.topbar{height:33px;background:var(--teal);display:flex;align-items:center;color:var(--white);font-size:9px;padding:0 0 0 96px;position:relative}
.topbar .item{display:flex;align-items:center;gap:5px;margin-right:115px}
.topbar .social{position:absolute;right:0;top:0;height:33px;width:160px;background:#1a1a1a;display:flex;gap:8px;justify-content:center;align-items:center}
.dot{width:11px;height:11px;border-radius:50%;background:var(--white);display:inline-block}
.nav{height:61px;display:flex;align-items:center;padding:0 76px 0 78px}
.brand{font-family:var(--body);font-weight:700;font-size:15px;color:var(--teal);display:flex;align-items:center;gap:6px;letter-spacing:.5px;white-space:nowrap;flex:none}
.brand i{width:12px;height:12px;background:var(--teal);display:inline-block}
.menu{display:flex;gap:11px;margin-left:24px;font-size:10px;color:var(--ink);white-space:nowrap;flex:none}
.menu a{color:inherit;text-decoration:none}
.menu a.on{color:var(--teal);border-bottom:1px solid var(--teal)}
.menu .sep{color:#bbb}
.btn{display:inline-flex;align-items:center;gap:6px;background:var(--teal);color:var(--white);border-radius:20px;font-size:9px;font-weight:600;padding:9px 17px;white-space:nowrap;flex:none}
.btn.light{background:var(--white);color:var(--teal)}
.nav .btn{margin-left:auto}

.photo{background:linear-gradient(135deg,#4b5a63,#8d9ba3 45%,#2f3d46);}
.photo.kitchen{background:linear-gradient(160deg,#c6ced3,#7f8c94 50%,#3a464e)}
.photo.chef{background:linear-gradient(150deg,#3b3f44,#9a8a7c 45%,#5b6a72)}

.hero{height:341px;position:relative}
.hero-card{position:absolute;left:13px;top:4px;width:347px;height:331px;background:var(--sky);border-radius:6px;padding:44px 0 0 64px}
.hero-card small{font-family:var(--head);color:var(--teal);font-weight:700;font-size:14px}
.hero-card h2{font-family:var(--head);font-weight:700;font-size:30px;line-height:1.22;margin:10px 0 16px}
.hero-card p{font-size:8.5px;color:var(--muted);line-height:1.7;width:255px}
.hero-card .ctas{display:flex;gap:8px;margin-top:27px}
.hero .photo{position:absolute;left:372px;top:4px;width:432px;height:331px;border-radius:6px 0 0 6px}

.ribbon-wrap{height:66px;position:relative;overflow:hidden}
.ribbon{position:absolute;left:-30px;width:880px;top:12px;height:40px;background:var(--teal);transform:rotate(-1.3deg);display:flex;align-items:center;gap:10px;color:var(--white);font-family:var(--head);font-weight:700;font-size:14px;white-space:nowrap;padding-left:20px}
.ribbon b{width:18px;height:18px;border:2px solid rgba(255,255,255,.7);border-radius:3px;display:inline-block;margin:0 8px}

.eyebrow{display:inline-block;font-size:8px;color:var(--teal);background:var(--sky-2);border-radius:10px;padding:3px 7px}
.eyebrow.dark{background:var(--white);color:var(--teal)}

.about{height:427px;position:relative}
.about .photo{position:absolute;left:16px;top:44px;width:327px;height:327px;border-radius:6px}
.about .badge{position:absolute;left:239px;top:273px;width:118px;height:118px;border-radius:12px;background:var(--teal);border:6px solid var(--white)}
.about-text{position:absolute;left:387px;top:15px;width:330px}
.about-text h2{font-family:var(--head);font-weight:600;font-size:27px;line-height:1.3;margin:9px 0 12px}
.about-text p{font-size:8.5px;color:var(--muted);line-height:1.75;margin-bottom:10px}
.about-text .btn{margin-top:6px}
.stats{display:flex;gap:60px;margin-top:26px}
.stats strong{font-family:var(--head);font-weight:600;font-size:24px;display:block}
.stats span{font-size:8px;color:var(--muted)}

.services{height:690px;background:var(--sky);position:relative;padding:30px 77px 0}
.services h2,.benefit-panel h2{font-family:var(--head);font-weight:700}
.services h2{font-size:26px;margin:8px 0 4px}
.services .lead{font-size:10px;color:var(--muted)}
.services .head-btn{position:absolute;right:77px;top:78px}
.grid{display:grid;grid-template-columns:repeat(3,197px);gap:30px 29px;margin-top:27px}
.card{height:233px;background:var(--white);border-radius:4px;padding:22px 14px;position:relative}
.card h3{font-family:var(--head);font-weight:600;font-size:15px;line-height:1.4;margin-bottom:12px}
.card p{font-size:8px;color:var(--muted);line-height:1.7}
.card .ico{position:absolute;left:14px;bottom:20px;width:38px;height:38px;border-radius:50%;background:var(--teal);display:flex;align-items:center;justify-content:center}
.card.active{background:var(--teal);color:var(--white)}
.card.active p{color:#d6e8ee}
.card.active .ico{background:var(--white)}
.card.pic{padding:0;overflow:hidden}
.card.pic .photo{width:100%;height:100%}

.benefits{height:460px;position:relative}
.benefits .photo{position:absolute;left:16px;top:52px;width:371px;height:370px;border-radius:8px}
.benefit-panel{position:absolute;left:409px;top:52px;width:369px;height:370px;background:var(--teal);border-radius:8px;color:var(--white);padding:14px 40px}
.benefit-panel h2{font-size:27px;line-height:1.35;margin:10px 0 8px;font-weight:600}
.benefit-panel p{font-size:8.5px;color:#cfe3ea;line-height:1.7}
.benefit-panel h4{font-size:10px;font-weight:600;margin:22px 0 14px}
.checks{display:grid;grid-template-columns:165px 1fr;gap:10px 0;font-size:10px;list-style:none}
.checks li{display:flex;gap:6px;line-height:1.4}
.checks li::before{content:"";flex:none;width:8px;height:8px;border:1px solid #9fc7d3;border-radius:50%;margin-top:3px}
.benefit-panel .btn{margin-top:20px}

.steps{height:185px;position:relative}
.steps-box{position:absolute;left:16px;top:12px;width:768px;height:154px;background:var(--sky);border-radius:6px;display:grid;grid-template-columns:245px 254px 1fr;padding:24px 0 0 61px}
.steps strong{font-family:var(--head);font-weight:600;color:var(--teal);font-size:27px;display:block}
.steps h5{color:var(--teal);font-size:10px;font-weight:600;margin:14px 0 6px}
.steps p{font-size:8px;color:var(--muted);line-height:1.7;width:150px}

.testimonials{height:389px;background:var(--teal-deep);color:var(--white);text-align:center;padding-top:40px;position:relative}
.testimonials h2{font-family:var(--head);font-weight:600;font-size:26px;margin:10px 0 4px}
.testimonials .sub{font-size:8.5px;color:#cfe3ea}
.quote{font-family:var(--head);font-weight:600;font-size:26px;line-height:1.4;width:560px;margin:38px auto 0;letter-spacing:.6px}
.arrow{position:absolute;top:243px;width:24px;height:24px;border:1px solid var(--white);border-radius:50%;display:flex;align-items:center;justify-content:center}
.author{display:flex;gap:8px;justify-content:center;align-items:center;margin-top:50px;font-size:8px;text-align:left}
.author .av{width:30px;height:30px;border-radius:50%;background:linear-gradient(135deg,#e8a24c,#b3592a)}

.contact{height:681px;position:relative;text-align:center;padding-top:59px}
.contact h2{font-family:var(--head);font-weight:600;font-size:27px;margin:14px 0 8px}
.contact .sub{font-size:9px;color:var(--muted)}
.contact .photo{position:absolute;left:80px;top:207px;width:318px;height:294px;border-radius:4px}
.info{position:absolute;left:80px;top:532px;display:grid;grid-template-columns:153px 160px;text-align:left}
.info .ci{width:30px;height:30px;border-radius:50%;background:var(--teal);margin-bottom:14px;display:flex;align-items:center;justify-content:center}
.info h6{font-size:10px;font-weight:600;margin-bottom:14px}
.info p{font-size:8.5px;color:var(--muted);line-height:2.2}
.form{position:absolute;left:407px;top:207px;width:320px;height:460px;background:var(--sky);border-radius:4px;padding:30px 30px;text-align:left}
.form h3{font-family:var(--head);font-weight:600;font-size:15px;margin-bottom:22px}
.form label{display:block;font-size:7px;margin-bottom:6px}
.field{background:var(--white);border-radius:12px;height:24px;font-size:7px;color:var(--muted);padding:7px 9px;margin-bottom:12px}
.row2{display:grid;grid-template-columns:1fr 1fr;gap:12px}
.field.area{height:90px;border-radius:8px}
.form .send{background:var(--teal);color:var(--white);border-radius:16px;height:31px;font-size:9px;font-weight:600;display:flex;align-items:center;justify-content:center;margin-top:20px}

.footer{height:222px;position:relative;font-size:9.5px}
.footer .brand{position:absolute;left:80px;top:52px;font-size:18px}
.footer .tag{position:absolute;left:80px;top:100px;width:150px;font-size:8.5px;line-height:1.7;color:#3a4a53}
.fcol{position:absolute;top:52px}
.fcol h6{font-size:11px;font-weight:500;margin-bottom:15px}
.fcol li{list-style:none;margin-bottom:9px;display:flex;gap:9px;align-items:flex-start}
.fsocial{position:absolute;left:704px;top:60px;display:flex;flex-direction:column;gap:10px}
.fsocial span{width:13px;height:13px;border-radius:3px;background:var(--ink)}
.legal{height:25px;background:var(--teal);color:var(--white);font-size:8px;display:flex;align-items:center;justify-content:center}

/* ===== mobile frame ===== */
.mob{position:absolute;left:909px;top:271px;width:172px;height:3718px;background:var(--white);overflow:hidden;font-size:5px}
.mob .m-top{height:20px;background:#1a1a1a;display:flex;gap:4px;justify-content:center;align-items:center}
.mob .m-top .dot{width:7px;height:7px}
.mob .m-nav{height:30px;display:flex;align-items:center;justify-content:space-between;padding:0 10px}
.mob .m-nav .brand{font-size:8px}
.burger{width:11px;height:8px;border-top:1.5px solid var(--ink);border-bottom:1.5px solid var(--ink);position:relative}
.burger::after{content:"";position:absolute;left:0;right:0;top:2px;border-top:1.5px solid var(--ink)}
.m-hero{margin:0 4px;height:172px;background:var(--sky);border-radius:4px;text-align:center;padding:18px 8px}
.m-hero small{color:var(--teal);font-weight:700;font-size:6px}
.m-hero h2{font-family:var(--head);font-size:13px;line-height:1.3;margin:7px 0}
.m-hero p{color:var(--muted);line-height:1.6}
.m-btns{display:flex;gap:4px;justify-content:center;margin-top:10px}
.m-btns span{background:var(--teal);color:var(--white);border-radius:8px;padding:3px 7px;font-size:4.5px}
.m-btns span.l{background:var(--white);color:var(--teal)}
.m-photo{margin:8px 6px;border-radius:4px}
.m-ribbon{height:25px;position:relative;overflow:hidden}
.m-ribbon div{position:absolute;left:-5px;width:190px;top:6px;height:10px;background:var(--teal);transform:rotate(-2deg);color:var(--white);font-size:4px;font-weight:700;white-space:nowrap;padding:2px 4px}
.m-sec{text-align:center;padding:8px 8px}
.m-sec h3{font-family:var(--head);font-size:11px;font-weight:600;line-height:1.3;margin:5px 0}
.m-sec p{color:var(--muted);line-height:1.6;margin-bottom:4px}
.m-sec .m-eyebrow,.m-benefit .m-eyebrow{display:inline-block;background:var(--sky-2);color:var(--teal);border-radius:5px;padding:1px 5px;font-size:4px}
.m-bar{height:9px;background:var(--teal);border-radius:5px;margin:6px 0;color:var(--white);font-size:4px;line-height:9px}
.m-stats{display:flex;gap:30px;justify-content:center;margin-top:8px}
.m-stats b{font-family:var(--head);font-size:10px;display:block;color:var(--ink)}
.m-about-photo{position:relative;margin:4px 8px;height:164px}
.m-about-photo .photo{width:150px;height:150px;border-radius:4px}
.m-about-photo i{position:absolute;right:4px;bottom:0;width:56px;height:56px;background:var(--teal);border:3px solid var(--white);border-radius:7px}
.m-services{background:var(--sky);padding:6px 6px 8px}
.m-card{height:178px;background:var(--white);border-radius:3px;padding:14px 10px;margin-bottom:10px;position:relative}
.m-card h4{font-family:var(--head);font-weight:600;font-size:9px;line-height:1.3;margin-bottom:6px}
.m-card p{color:var(--muted);line-height:1.6}
.m-card .ico{position:absolute;left:10px;bottom:16px;width:22px;height:22px;border-radius:50%;background:var(--teal)}
.m-card.active{background:var(--teal);color:var(--white)}
.m-card.active p{color:#d6e8ee}
.m-card.active .ico{background:var(--white)}
.m-card.pic{padding:0;overflow:hidden}
.m-card.pic .photo{height:100%}
.m-benefit{margin:6px 6px;height:160px;background:var(--teal);border-radius:4px;color:var(--white);padding:10px 10px;text-align:center}
.m-benefit h4{font-family:var(--head);font-size:9px;line-height:1.3;margin:5px 0}
.m-benefit p{color:#cfe3ea;line-height:1.5}
.m-benefit ul{display:grid;grid-template-columns:1fr 1fr;gap:4px;list-style:none;text-align:left;margin:8px 0;font-size:4px}
.m-steps{margin:4px 6px;height:312px;background:var(--sky);border-radius:4px;text-align:center;padding:14px 16px}
.m-steps b{font-family:var(--head);color:var(--teal);font-size:14px;display:block;margin-top:10px}
.m-steps h6{color:var(--teal);font-size:5.5px;margin:5px 0 3px}
.m-steps p{color:var(--muted);line-height:1.6}
.m-test{height:85px;background:var(--teal-deep);color:var(--white);text-align:center;padding:10px 18px;margin-top:10px}
.m-test h6{font-size:4.5px;margin-bottom:8px}
.m-test p{font-family:var(--head);font-weight:700;font-size:5px;line-height:1.5}
.m-form{margin:8px 8px;height:250px;background:var(--sky);border-radius:3px;padding:10px 10px;text-align:left}
.m-form h5{font-size:5.5px;margin-bottom:8px}
.m-form .f{background:var(--white);border-radius:5px;height:9px;margin-bottom:8px;font-size:3.5px;color:var(--muted);padding:2px 4px}
.m-form .f.area{height:42px;border-radius:3px}
.m-form .s{background:var(--teal);color:var(--white);border-radius:5px;height:12px;font-size:4px;display:flex;align-items:center;justify-content:center;margin-top:10px}
.m-info{display:grid;grid-template-columns:1fr 1fr;padding:6px 12px;height:66px;line-height:1.6}
.m-info i{display:block;width:12px;height:12px;border-radius:50%;background:var(--teal);margin-bottom:5px}
.m-footer{height:251px;text-align:center;padding:24px 8px 0;position:relative}
.m-footer .brand{justify-content:center;font-size:11px}
.m-footer .tag{color:#3a4a53;line-height:1.6;margin:10px 14px 0}
.m-fcols{display:grid;grid-template-columns:1fr 1.4fr;text-align:left;margin-top:24px;line-height:2}
.m-fcols h6{font-size:5px;font-weight:600}
.m-fsoc{display:flex;gap:5px;justify-content:center;margin-top:16px}
.m-fsoc span{width:8px;height:8px;background:var(--ink);border-radius:2px}
.m-legal{height:25px;background:var(--teal);color:var(--white);display:flex;align-items:center;justify-content:center;font-size:4.5px}
</style>
</head>
<body>

<header class="board-title">
  <h1>HEARTHLINE Website :</h1>
  <p>UX / UI Design &amp; Frontend Developing.</p>
</header>
<div class="tools" aria-hidden="true"><span></span><span></span><span></span><span></span><span></span></div>

<!-- Desktop page -->
<main class="desk">
  <div class="topbar">
    <span class="item">
      <svg width="10" height="8" viewBox="0 0 10 8"><rect x=".5" y=".5" width="9" height="7" fill="none" stroke="#fff"/><path d="M.5 .5 5 4.5 9.5 .5" fill="none" stroke="#fff"/></svg>
      support@hearthline.com</span>
    <span class="item">
      <svg width="9" height="9" viewBox="0 0 10 10"><path d="M2 1l2 2-1 1.5a6 6 0 0 0 2.5 2.5L7 6l2 2-1.2 1.2C4.5 9 1 5.5.8 2.2Z" fill="#fff"/></svg>
      +1 (800) 555-0148</span>
    <div class="social"><span class="dot"></span><span class="dot"></span><span class="dot"></span><span class="dot"></span></div>
  </div>

  <nav class="nav">
    <div class="brand"><i></i>HEARTHLINE</div>
    <div class="menu">
      <a class="on" href="#">Home</a><span class="sep">|</span>
      <a href="#">About</a><span class="sep">|</span>
      <a href="#">Services</a><span class="sep">|</span>
      <a href="#">Testimonials</a><span class="sep">|</span>
      <a href="#">Contact</a>
    </div>
    <a class="btn">Call +1 (800) 555-0148 →</a>
  </nav>

  <section class="hero">
    <div class="hero-card">
      <small>Welcome to Hearthline</small>
      <h2>Reliable Kitchen<br>Equipment Repair<br>You Can Trust</h2>
      <p>We keep your commercial kitchen running with fast, reliable support and expert maintenance to reduce downtime and ensure safety.</p>
      <div class="ctas"><span class="btn">Call +1 (800) 555-0148 →</span><span class="btn light">Request Now →</span></div>
    </div>
    <div class="photo" role="img" aria-label="Technician and chef bumping fists in a commercial kitchen"></div>
  </section>

  <div class="ribbon-wrap"><div class="ribbon">ns <b></b>Kitchen Equipment Repairs <b></b>Preventive Maintenance <b></b>Installation &amp; Setup <b></b>Drain c</div></div>

  <section class="about">
    <div class="photo chef" role="img" aria-label="Chef working at a stainless steel kitchen station"></div>
    <div class="badge"></div>
    <div class="about-text">
      <span class="eyebrow">out Us – About Us</span>
      <h2>Your Trusted Partner in<br>Kitchen Equipment Repair</h2>
      <p>At Hearthline, we specialize in the maintenance and repair of commercial kitchen equipment, helping restaurants, cafes, hotels, and other food-service businesses keep their operations running smoothly.</p>
      <p>Our team of skilled technicians delivers fast, reliable, and expert service to minimize downtime, ensure safety, and maintain compliance with industry standards.</p>
      <p>We pride ourselves on being a trusted partner for businesses that rely on well-functioning kitchen equipment to serve their customers efficiently.</p>
      <span class="btn">Get Started Today →</span>
      <div class="stats"><div><strong>15+</strong><span>Years of experience</span></div><div><strong>98%</strong><span>Satisfaction rate</span></div></div>
    </div>
  </section>

  <section class="services">
    <span class="eyebrow">rvices – Our service</span>
    <h2>What we do</h2>
    <p class="lead">Comprehensive solutions for commercial kitchen equipment</p>
    <span class="btn head-btn">We're Here to Help →</span>
    <div class="grid">
      <article class="card active"><h3>Preventive Maintenance</h3><p>Regular inspections and servicing to extend equipment lifespan and avoid unexpected breakdowns.</p><span class="ico"><svg width="16" height="16" viewBox="0 0 16 16"><circle cx="8" cy="8" r="5" fill="none" stroke="#0e6478" stroke-width="1.5"/><path d="M8 5v3l2 1" stroke="#0e6478" fill="none"/></svg></span></article>
      <article class="card"><h3>Emergency Repairs</h3><p>Fast, reliable response to get your kitchen back up and running with minimal downtime.</p><span class="ico"><svg width="16" height="16" viewBox="0 0 16 16"><circle cx="8" cy="8" r="5" fill="none" stroke="#fff" stroke-width="1.5"/><path d="M8 5v3l2 1" stroke="#fff" fill="none"/></svg></span></article>
      <article class="card"><h3>Installation &amp; Setup</h3><p>Professional installation of new kitchen equipment for optimal performance and compliance.</p><span class="ico"><svg width="16" height="16" viewBox="0 0 16 16"><circle cx="8" cy="8" r="3" fill="none" stroke="#fff" stroke-width="1.5"/><circle cx="8" cy="8" r="6" fill="none" stroke="#fff" stroke-dasharray="2 2"/></svg></span></article>
      <article class="card"><h3>Safety &amp; Compliance Inspections</h3><p>Ensuring your equipment meets all health and safety regulations.</p><span class="ico"><svg width="16" height="16" viewBox="0 0 16 16"><path d="M8 2l5 2v4c0 3-2.5 5-5 6-2.5-1-5-3-5-6V4Z" fill="none" stroke="#fff" stroke-width="1.5"/><path d="M5.5 8l2 2 3-3.5" fill="none" stroke="#fff"/></svg></span></article>
      <article class="card"><h3>Equipment Upgrades &amp; Replacement</h3><p>Modernizing outdated equipment to improve efficiency and safety.</p><span class="ico"><svg width="16" height="16" viewBox="0 0 16 16"><path d="M3 13l7-7M10 3l3 3M3 3l10 10" stroke="#fff" stroke-width="1.5" fill="none"/></svg></span></article>
      <article class="card pic"><div class="photo" role="img" aria-label="Technician servicing a commercial oven"></div></article>
    </div>
  </section>

  <div class="ribbon-wrap"><div class="ribbon">ns <b></b>Kitchen Equipment Repairs <b></b>Preventive Maintenance <b></b>Installation &amp; Setup <b></b>Drain c</div></div>

  <section class="benefits">
    <div class="photo kitchen" role="img" aria-label="Clean stainless steel commercial kitchen line"></div>
    <div class="benefit-panel">
      <span class="eyebrow dark">nefits – Benefits – B</span>
      <h2>Fast response when you need it most</h2>
      <p>We understand that kitchen downtime means lost revenue. Our expert technicians arrive quickly to restore your equipment.</p>
      <h4>Here's why businesses trust Hearthline:</h4>
      <ul class="checks">
        <li>Reliable &amp; Fast<br>Response</li><li>Comprehensive<br>Solutions</li>
        <li>Expert Technicians</li><li>Technical Support &amp;<br>Troubleshooting</li>
        <li>Safety &amp; Compliance<br>Focused</li>
      </ul>
      <span class="btn light">Request Service Now →</span>
    </div>
  </section>

  <section class="steps">
    <div class="steps-box">
      <div><strong>01</strong><h5>Book your appointment</h5><p>Contact us via phone or online to schedule your kitchen equipment service at a time that suits you.</p></div>
      <div><strong>02</strong><h5>Inspection &amp; service</h5><p>Our certified technicians arrive on time to inspect, diagnose, and service your equipment efficiently.</p></div>
      <div><strong>03</strong><h5>Follow-up &amp; support</h5><p>We provide ongoing support and maintenance to keep your kitchen running smoothly.</p></div>
    </div>
  </section>

  <section class="testimonials">
    <span class="eyebrow dark">ionials – Testimonial</span>
    <h2>Client stories</h2>
    <p class="sub">What our clients say about our service</p>
    <p class="quote">Professional, efficient, and they truly understand the importance of kitchen operations.</p>
    <span class="arrow" style="left:94px"><svg width="9" height="9" viewBox="0 0 10 10"><path d="M9 5H1M4 2 1 5l3 3" stroke="#fff" fill="none"/></svg></span>
    <span class="arrow" style="right:94px"><svg width="9" height="9" viewBox="0 0 10 10"><path d="M1 5h8M6 2l3 3-3 3" stroke="#fff" fill="none"/></svg></span>
    <div class="author"><span class="av" role="img" aria-label="Client portrait"></span><div><b>Daniel Reyes</b><br>Head chef, Harbor Table</div></div>
  </section>

  <section class="contact">
    <span class="eyebrow">act Us – Contact Us</span>
    <h2>Let's Get in Touch</h2>
    <p class="sub">Keep your kitchen running smoothly with Hearthline's expert service.</p>
    <div class="photo chef" role="img" aria-label="Smiling chef in a white jacket"></div>
    <div class="info">
      <div><span class="ci"><svg width="12" height="10" viewBox="0 0 10 8"><rect x=".5" y=".5" width="9" height="7" fill="none" stroke="#fff"/><path d="M.5 .5 5 4.5 9.5 .5" fill="none" stroke="#fff"/></svg></span><h6>Office Email</h6><p>info@hearthline.com<br>support@hearthline.com</p></div>
      <div><span class="ci"><svg width="10" height="12" viewBox="0 0 10 12"><path d="M5 11S1 7 1 4.5a4 4 0 0 1 8 0C9 7 5 11 5 11Z" fill="none" stroke="#fff"/><circle cx="5" cy="4.5" r="1.4" fill="#fff"/></svg></span><h6>Our Location</h6><p>48 Mill Street, Fairview,<br>Texas, United States.</p></div>
    </div>
    <form class="form">
      <h3>Send a Message</h3>
      <div class="row2"><div><label>First Name*</label><div class="field">First Name</div></div><div><label>Last Name*</label><div class="field">Last Name</div></div></div>
      <label>Phone Number*</label><div class="field">Phone Number</div>
      <label>Email Address*</label><div class="field">Email Address</div>
      <label>Short Message*</label><div class="field area">How Can We Help You?</div>
      <div class="send">Send Message</div>
    </form>
  </section>

  <div class="ribbon-wrap" style="height:74px"><div class="ribbon">ns <b></b>Kitchen Equipment Repairs <b></b>Preventive Maintenance <b></b>Installation &amp; Setup <b></b>Drain c</div></div>

  <footer class="footer">
    <div class="brand"><i></i>HEARTHLINE</div>
    <p class="tag">Reliable commercial kitchen equipment repair — keeping your business running smoothly.</p>
    <div class="fcol" style="left:353px"><h6>Quick Links</h6><ul><li>Home</li><li>About</li><li>Services</li><li>Testimonials</li></ul></div>
    <div class="fcol" style="left:486px"><h6>Contact Us</h6><ul>
      <li><svg width="9" height="9" viewBox="0 0 10 10"><path d="M2 1l2 2-1 1.5a6 6 0 0 0 2.5 2.5L7 6l2 2-1.2 1.2C4.5 9 1 5.5.8 2.2Z" fill="#14212b"/></svg>201-555-0190</li>
      <li><svg width="8" height="10" viewBox="0 0 10 12"><path d="M5 11S1 7 1 4.5a4 4 0 0 1 8 0C9 7 5 11 5 11Z" fill="#14212b"/></svg>210 Orchard Road, Dayton<br>OH 45402</li>
      <li><svg width="10" height="8" viewBox="0 0 10 8"><rect width="10" height="8" fill="#14212b"/></svg>support@hearthline.com</li></ul></div>
    <div class="fsocial"><span></span><span></span><span></span><span></span></div>
  </footer>
  <div class="legal">© 2025 hearthline. All rights reserved.</div>
</main>

<!-- Mobile page -->
<aside class="mob">
  <div class="m-top"><span class="dot"></span><span class="dot"></span><span class="dot"></span><span class="dot"></span></div>
  <div class="m-nav"><div class="brand"><i style="width:7px;height:7px"></i>HEARTHLINE</div><span class="burger"></span></div>
  <div class="m-hero">
    <small>Welcome to Hearthline</small>
    <h2>Reliable Kitchen Equipment Repair You Can Trust</h2>
    <p>We keep your commercial kitchen running with fast, reliable support and expert maintenance to reduce downtime.</p>
    <div class="m-btns"><span>Call +1 (800) 555-0148 →</span><span class="l">Request Now →</span></div>
  </div>
  <div class="m-photo photo" style="height:136px" role="img" aria-label="Technician and chef bumping fists in a kitchen"></div>
  <div class="m-ribbon"><div>Kitchen Equipment Repairs ▢ Preventive Maintenance ▢ Installation &amp; Setup</div></div>
  <div class="m-sec" style="height:197px">
    <span class="m-eyebrow">Us – About</span>
    <h3>Your Trusted Partner in Kitchen Equipment Repair</h3>
    <p>At Hearthline, we specialize in the maintenance and repair of commercial kitchen equipment for restaurants, cafes and hotels.</p>
    <p>Our skilled technicians deliver fast, reliable and expert service to minimize downtime and maintain compliance.</p>
    <p>We are a trusted partner for businesses that rely on well-functioning kitchen equipment.</p>
    <div class="m-bar">Get Started Today →</div>
    <div class="m-stats"><div><b>15+</b>Years of experience</div><div><b>98%</b>Satisfaction rate</div></div>
  </div>
  <div class="m-about-photo"><div class="photo chef" role="img" aria-label="Chef at a kitchen station"></div><i></i></div>
  <div class="m-sec" style="height:90px">
    <span class="m-eyebrow">rvices – Service</span>
    <h3>What we do</h3>
    <p>Comprehensive solutions for commercial kitchen equipment</p>
    <div class="m-bar">We're Here to Help →</div>
  </div>
  <div class="m-services">
    <div class="m-card active"><h4>Preventive Maintenance</h4><p>Regular inspections and servicing to extend equipment lifespan and avoid unexpected breakdowns.</p><span class="ico"></span></div>
    <div class="m-card"><h4>Emergency Repairs</h4><p>Fast, reliable response to get your kitchen back up and running with minimal downtime.</p><span class="ico"></span></div>
    <div class="m-card"><h4>Installation &amp; Setup</h4><p>Professional installation of new kitchen equipment for optimal performance and compliance.</p><span class="ico"></span></div>
    <div class="m-card"><h4>Safety &amp; Compliance Inspections</h4><p>Ensuring your equipment meets all health and safety regulations.</p><span class="ico"></span></div>
    <div class="m-card"><h4>Equipment Upgrades &amp; Replacement</h4><p>Modernizing outdated equipment to improve efficiency and safety.</p><span class="ico"></span></div>
    <div class="m-card pic"><div class="photo" role="img" aria-label="Technician servicing an oven"></div></div>
  </div>
  <div class="m-ribbon"><div>Kitchen Equipment Repairs ▢ Preventive Maintenance ▢ Installation &amp; Setup</div></div>
  <div class="m-benefit">
    <span class="m-eyebrow">nefits – Benefits</span>
    <h4>Fast response when you need it most</h4>
    <p>We understand that kitchen downtime means lost revenue. Our technicians arrive quickly.</p>
    <p style="margin-top:5px;color:#fff">Here's why businesses trust Hearthline:</p>
    <ul><li>Reliable &amp; Fast Response</li><li>Comprehensive Solutions</li><li>Expert Technicians</li><li>Technical Support &amp; Troubleshooting</li><li>Safety &amp; Compliance Focused</li></ul>
    <div class="m-btns"><span class="l">Request Service Now →</span></div>
  </div>
  <div class="m-photo photo kitchen" style="height:158px" role="img" aria-label="Stainless steel commercial kitchen"></div>
  <div class="m-steps">
    <b>01</b><h6>Book your appointment</h6><p>Contact us via phone or online to schedule your kitchen equipment service at a time that suits you.</p>
    <b>02</b><h6>Inspection &amp; service</h6><p>Our certified technicians arrive on time to inspect, diagnose, and service your equipment efficiently.</p>
    <b>03</b><h6>Follow-up &amp; support</h6><p>We provide ongoing support and maintenance to keep your kitchen running smoothly.</p>
  </div>
  <div class="m-test"><h6>Client stories</h6><p>Professional, efficient, and they truly understand the importance of kitchen operations.</p></div>
  <div class="m-sec" style="height:55px;padding-top:14px">
    <span class="m-eyebrow">act Us – Contact</span>
    <h3>Let's Get in Touch</h3>
    <p>Keep your kitchen running smoothly with Hearthline.</p>
  </div>
  <div class="m-form">
    <h5>Send a Message</h5>
    <div style="display:grid;grid-template-columns:1fr 1fr;gap:5px"><div class="f">First Name</div><div class="f">Last Name</div></div>
    <div class="f">Phone Number</div><div class="f">Email Address</div><div class="f area">How Can We Help You?</div>
    <div class="s">Send Message</div>
  </div>
  <div class="m-photo photo chef" style="height:140px" role="img" aria-label="Smiling chef"></div>
  <div class="m-info"><div><i></i><b>Office Email</b><br>info@hearthline.com<br>support@hearthline.com</div><div><i></i><b>Our Location</b><br>48 Mill Street, Fairview,<br>Texas, United States.</div></div>
  <div class="m-ribbon"><div>Kitchen Equipment Repairs ▢ Preventive Maintenance ▢ Installation &amp; Setup</div></div>
  <div class="m-footer">
    <div class="brand"><i style="width:9px;height:9px"></i>HEARTHLINE</div>
    <p class="tag">Reliable commercial kitchen equipment repair — keeping your business running smoothly.</p>
    <div class="m-fcols"><div><h6>Quick Links</h6>Home<br>About<br>Services<br>Testimonials</div><div><h6>Contact Us</h6>201-555-0190<br>210 Orchard Road, Dayton<br>OH 45402<br>support@hearthline.com</div></div>
    <div class="m-fsoc"><span></span><span></span><span></span><span></span></div>
  </div>
  <div class="m-legal">© 2025 hearthline. All rights reserved.</div>
</aside>

</body>
</html>
```